International Book about Player ethics in stadiums - This book will be presented to players in all

This book will be distributed to players to learn about the mathematical ethics, and the spirit of sport required for the ideal player
It also aims to teach the public the morals of encouragement and some instructions about keeping the playgrounds beautiful
Size : w 15 x 21 H
Title of the book
ظلال النخيل عند الغروب
Author
تاليف / الدكتور نادر عادل المرزوقي
1440-2018

Target Market(s)

This book will be presented to players in all activities

Colors

Designer to choose colors to be used in the design.

Requirements
Must have
• Selected colors must be related to play, players, activity and vitality.
• To be the attractive design makes the book lovable
• Final design of the file in the front and back should be on files illustrator and Photoshop and accept the opening on the lower versions
•  
Nice to have
• Example:
• Option 1
• stadium image
• The image must be for a mathematical expression
• For example: a player extends his hand to the opponent to help him from the ground or
• Two players from the two teams are hugging - shaking hands
• Option 2
• The picture can be a sports track
• On both sides of the track are the names of sports ethics - fair play - sportsmanship - compassion - clean encouragement - discipline - respect - apology ... etc
Should not have
• Direct images of famous players or people
• In the case of images should be indirect - or possible to be drawings
• Direct photos of famous people or players are not required

```html
<!DOCTYPE html>
<html lang="ar">
<head>
<meta charset="utf-8">
<title>ظلال النخيل عند الغروب — غلاف الكتاب</title>
<link rel="stylesheet" href="https://fonts.googleapis.com/css2?family=Cairo:wght@700;900&family=Montserrat:wght@600&family=Oswald:wght@700&display=swap">
<style>
  :root {
    --backdrop: #d6ebf7;
    --track-red: #b8432c;
    --track-red-dark: #9c3522;
    --lane-line: #ffffff;
    --title-stroke: #6b1a1e;
    --stadium-top: #c98a7a;
    --stadium-mid: #b96a55;
    --stadium-field: #8a6a3c;
    --stadium-track: #c0533a;
    --text-light: #ffffff;
  }
  * { margin: 0; padding: 0; box-sizing: border-box; }
  html, body {
    width: 1200px; height: 1200px; overflow: hidden;
    background: var(--backdrop);
  }
  .canvas {
    position: relative; width: 1200px; height: 1200px;
  }
  .book-cover {
    position: absolute; left: 240px; top: 60px;
    width: 720px; height: 1080px;
    background: var(--track-red);
    overflow: hidden;
  }
  .lanes {
    position: absolute; left: 0; top: 0; width: 100%; height: 637px;
    display: flex; flex-direction: column;
  }
  .lane {
    position: relative; flex: 1;
    background: linear-gradient(180deg, var(--track-red-dark) 0%, var(--track-red) 40%, var(--track-red) 100%);
    border-bottom: 9px solid var(--lane-line);
    display: flex; align-items: center;
  }
  .lane-name {
    direction: ltr;
    margin-left: 52px;
    font-family: "Montserrat", sans-serif; font-weight: 600;
    font-size: 27px; color: var(--text-light);
    text-shadow: 0 1px 2px rgba(0,0,0,.35);
  }
  .lane-marker {
    position: absolute; left: 570px; top: 6px; bottom: 6px;
    width: 9px; background: var(--lane-line);
  }
  .lane-number {
    position: absolute; left: 590px; width: 130px; top: 0; bottom: 0;
    display: flex; align-items: center; justify-content: center;
    font-family: "Oswald", sans-serif; font-weight: 700;
    font-size: 76px; line-height: 1; color: var(--text-light);
    -webkit-text-stroke: 2px #5a1a14;
    text-shadow: 2px 3px 0 rgba(60,15,10,.6);
  }
  .stadium-scene {
    position: absolute; left: 0; top: 637px; width: 100%; height: 443px;
    background:
      linear-gradient(180deg, var(--stadium-top) 0%, var(--stadium-mid) 38%, var(--stadium-field) 62%, var(--stadium-track) 72%, var(--track-red) 100%);
  }
  .book-title {
    position: absolute; left: 0; top: 665px; width: 100%;
    text-align: center;
    font-family: "Cairo", sans-serif; font-weight: 900;
    font-size: 92px; line-height: 136px;
    color: var(--text-light);
    -webkit-text-stroke: 3px var(--title-stroke);
    paint-order: stroke fill;
    text-shadow: 4px 5px 0 var(--title-stroke);
  }
  .book-author {
    position: absolute; left: 0; top: 980px; width: 100%;
    text-align: center;
    font-family: "Cairo", sans-serif; font-weight: 700;
    font-size: 30px; color: var(--text-light);
    text-shadow: 0 2px 3px rgba(0,0,0,.5);
  }
</style>
</head>
<body>
<div class="canvas">
  <div class="book-cover">
    <div class="lanes">
      <div class="lane"><span class="lane-name">Fair Play</span><span class="lane-marker"></span><span class="lane-number">1</span></div>
      <div class="lane"><span class="lane-name">Sportsmanship</span><span class="lane-marker"></span><span class="lane-number">2</span></div>
      <div class="lane"><span class="lane-name">Compassion</span><span class="lane-marker"></span><span class="lane-number">3</span></div>
      <div class="lane"><span class="lane-name">Clean Encouragement</span><span class="lane-marker"></span><span class="lane-number">4</span></div>
      <div class="lane"><span class="lane-name">Discipline</span><span class="lane-marker"></span><span class="lane-number">5</span></div>
      <div class="lane"><span class="lane-name">Respect</span><span class="lane-marker"></span><span class="lane-number">6</span></div>
      <div class="lane"><span class="lane-name">Apology</span><span class="lane-marker"></span><span class="lane-number">7</span></div>
    </div>
    <div class="stadium-scene" role="img" aria-label="Photo of an athletics stadium with stands and a red running track under a cloudy sky"></div>
    <h1 class="book-title">ظلال النخيل<br>عند الغروب</h1>
    <p class="book-author">المؤلف/الدكتور نادر عادل المرزوقي</p>
  </div>
</div>
</body>
</html>
```